Swiss VPS hosting website for local hosting provider

Hi,

Need a new website which includes the same pages as todays website under https://www.kelvaport.ch

Those include:
Homepage
Product pages
Blog
Contact page

There should be a mobile version as well

Coding will be done on drupal.

Looking for a fresh design which fit to VPS hosting. Other examples are brantiq.ch which I very much like. Very plain and not a lot of not needed stuff.

Target Market(s)

Switzerland, VPS Hosting

Industry/Entity Type

Product

Number of Pages Required

4 page

Font styles to use
Sans Serif

Requirements
Must have
• Same sites as the original site

```html
<!DOCTYPE html>
<html lang="en">
<head>
<meta charset="utf-8">
<title>Kelvaport – Solid Swiss Hosting</title>
<link rel="stylesheet" href="https://fonts.googleapis.com/css2?family=Montserrat:wght@400;600;700;800&family=Open+Sans:wght@400;600;700&display=swap">
<style>
:root{
  --red:#d8251c;
  --ink:#2a2f34;
  --nav:#22272b;
  --band:#2d3338;
  --grey-1:#e9ebec;
  --grey-2:#d6d9db;
  --grey-3:#c5c9cc;
  --text:#4a4f54;
  --teal:#2da489;
  --green:#26b07f;
  --yellow:#f5c518;
  --orange:#f29b11;
  --blue:#1f6fc4;
  --white:#ffffff;
  --footer:#24282c;
}
*{box-sizing:border-box;margin:0;padding:0}
html,body{width:1200px;height:3696px;overflow:hidden}
body{font-family:"Open Sans",Arial,sans-serif;color:var(--text);background:var(--white);position:relative}
.abs{position:absolute}
.heading{font-family:"Montserrat",Arial,sans-serif;font-weight:700;color:var(--ink);text-transform:uppercase;text-align:center;letter-spacing:.5px}
.rule{width:110px;height:2px;background:var(--ink);margin:14px auto 0}

.topbar{top:0;left:0;width:1200px;height:74px;background:var(--red);color:var(--white);font-size:13px}
.brand{left:79px;top:20px;height:34px;padding:0 10px;border:2px solid var(--white);font-family:"Montserrat",sans-serif;font-weight:700;font-size:22px;line-height:30px;letter-spacing:.5px}
.topbar .item{top:29px;display:flex;align-items:center;gap:7px}
.mainnav{top:74px;left:0;width:1200px;height:44px;background:var(--nav);display:flex;justify-content:center;gap:30px;font-size:13px;color:#d5d8db;line-height:44px}
.mainnav a{color:inherit;text-decoration:none}
.mainnav .active{color:var(--white);font-weight:700;border-bottom:2px solid var(--white);line-height:30px;margin-top:6px;height:32px}

.hero{top:118px;left:0;width:1200px;height:264px;background:linear-gradient(180deg,#f4f5f5,#e4e6e7)}
.hero h1{position:absolute;top:46px;width:100%;text-align:center;font-family:"Montserrat",sans-serif;font-weight:800;font-size:64px;color:var(--red);letter-spacing:1px}
.hero p{position:absolute;top:128px;left:405px;width:390px;text-align:center;font-size:14px;line-height:21px;color:#555}
.hero p b{color:#333}
.dots{top:216px;left:573px;display:flex;gap:6px}
.dots span{width:9px;height:9px;border-radius:50%;border:1.5px solid #e58f8a}
.dots span.on{background:var(--red);border-color:var(--red)}

.strip{top:382px;left:0;width:1200px;height:86px;background:var(--band)}
.tiles{top:382px;left:81px;width:1035px;height:86px;display:grid;grid-template-columns:repeat(6,1fr)}
.tile{padding-top:14px;text-align:center;font-size:12px;line-height:16px;color:#333}
.tile:nth-child(odd){background:var(--grey-1)}
.tile:nth-child(even){background:var(--grey-3)}
.tile svg{display:block;margin:0 auto 6px}

.sec-title-1{top:532px;width:1200px}
.tabs{top:608px;left:291px;display:flex;border:1px solid #d2d5d7}
.tabs span{font-size:12px;padding:0 18px;line-height:32px;border-right:1px solid #d2d5d7;color:#444}
.tabs span:last-child{border-right:0}
.tabs .on{background:var(--red);color:var(--white)}
.card{top:697px;width:222px;height:345px;background:var(--grey-2);box-shadow:0 2px 4px rgba(0,0,0,.15)}
.card .head{height:70px;background:var(--band);color:var(--white);position:relative;padding:16px 0 0 10px;font-size:12.5px;line-height:16px;font-weight:600;text-transform:uppercase}
.card .price{position:absolute;right:10px;top:8px;width:72px;height:56px;border:1px solid #6d7479;text-align:center;color:var(--white)}
.card .price .cur{position:absolute;left:6px;top:3px;font-size:13px}
.card .price .num{font-family:"Montserrat",sans-serif;font-weight:800;font-size:32px;line-height:42px}
.card .price .per{display:block;font-size:8px;line-height:8px;text-transform:none;font-weight:400}
.card ul{list-style:none}
.card li{height:33px;line-height:33px;text-align:center;font-size:12px;color:#444;border-bottom:1px solid #c4c8cb}
.card li:nth-child(even){background:#dfe2e3}
.card .buy{height:44px;line-height:44px;background:var(--red);color:var(--white);text-align:center;font-weight:700;font-size:13px;text-transform:uppercase}
.btn-green{background:var(--green);color:var(--white);text-align:center;font-size:13px;border-radius:3px;box-shadow:0 2px 0 #1b8a62}

.helpbar{top:1207px;left:0;width:1200px;height:62px;background:var(--band);color:var(--white);font-family:"Montserrat",sans-serif;font-size:19px;font-weight:600}
.helpbar .item{top:19px;display:flex;align-items:center;gap:10px}

.sec-title-2{top:1318px;width:1200px}
.ben-head-red{top:1456px;left:81px;width:693px;height:54px;background:var(--red);color:var(--white);text-align:center;line-height:54px;font-size:15px;font-weight:600}
.ben-head-dark{top:1456px;left:774px;width:342px;height:54px;background:var(--band);color:var(--white);text-align:center;padding-top:8px;font-size:14px;line-height:19px;font-weight:600}
.ben{top:1510px;width:172px;height:185px;background:var(--grey-2);text-align:center;padding:0 12px;font-size:12px;line-height:16px;color:#333}
.ben:nth-child(even){background:var(--grey-1)}
.ben .icon{width:46px;height:46px;border-radius:50%;background:var(--band);margin:20px auto 12px;display:flex;align-items:center;justify-content:center}
.ben .n{position:absolute;top:6px;right:6px;width:15px;height:15px;border-radius:50%;background:#9aa0a5;color:var(--white);font-size:9px;line-height:15px}
.ben .more{color:var(--red)}
.ben-pop{top:1526px;left:772px;width:176px;height:196px;background:var(--band);color:var(--white);text-align:center;font-size:11.5px;line-height:15px;padding:12px 10px;box-shadow:0 3px 8px rgba(0,0,0,.3)}
.about-link{top:1830px;width:1200px;text-align:center;font-size:11px;color:#555}

.offshore{top:1917px;left:0;width:1200px;height:411px;background:radial-gradient(ellipse at 50% 45%,#3a4249,#2b3238 70%)}
.offshore .heading{position:absolute;top:66px;width:100%;color:var(--white);font-size:26px}
.offshore .rule{background:var(--white)}
.flags{top:166px;left:570px;display:flex;gap:8px}
.offshore .sub{position:absolute;top:200px;width:100%;text-align:center;color:var(--teal);font-size:15px;font-weight:600}
.offshore ul{position:absolute;top:244px;left:356px;width:500px;color:#e2e5e7;font-size:13px;line-height:19px;list-style:none}
.offshore li{position:relative;padding-left:18px;margin-bottom:12px}
.offshore li:before{content:"";position:absolute;left:2px;top:7px;width:5px;height:5px;border-radius:50%;background:var(--white)}
.notch{left:588px;width:0;height:0;border-left:12px solid transparent;border-right:12px solid transparent}

.aswell{top:2328px;left:0;width:1200px;height:247px;background:var(--teal);color:var(--white);text-align:center}
.aswell h3{margin-top:55px;font-size:16px;font-weight:600}
.aswell p{font-size:12.5px;line-height:22px;margin-top:14px}

.sec-title-3{top:2640px;width:1200px}
.post{top:2718px;width:372px}
.post .avatar{position:absolute;left:0;top:0;width:38px;height:38px;border-radius:50%;background:linear-gradient(135deg,#b9bcbf,#7d8287)}
.post h4{margin-left:56px;font-family:"Montserrat",sans-serif;font-weight:700;font-size:22px;color:var(--ink)}
.post .meta{margin-left:56px;font-size:10.5px;color:#777;display:flex;gap:8px;align-items:center}
.post .meta b{color:var(--red);font-weight:400}
.post .body{margin-top:16px;font-size:12.5px;line-height:21px;color:#555}
.post .read{text-align:right;font-size:10.5px;color:var(--red);margin-top:8px}
.arrow{top:2780px;color:#aaa;font-size:28px}

.promo{top:2944px;left:0;width:1200px;height:87px;background:repeating-linear-gradient(180deg,var(--yellow) 0 12px,var(--orange) 12px 15px)}
.promo .mid{position:absolute;top:16px;left:0;width:1200px;height:55px;background:var(--yellow)}
.badge{top:2934px;left:222px;width:160px;height:106px;background:var(--red);border:4px solid #f3ded7;display:flex;align-items:center;justify-content:center}
.badge .inner{width:114px;height:70px;background:var(--white);display:flex;align-items:center;justify-content:center;gap:2px;color:var(--red);font-family:"Montserrat",sans-serif;font-weight:800;font-size:40px}
.badge .inner small{font-size:11px;line-height:12px;display:block}
.promo-text{top:2968px;left:455px;font-family:"Montserrat",sans-serif;font-weight:700;font-size:30px;line-height:38px;color:var(--ink)}
.promo-btn{top:2972px;left:890px;width:108px;height:30px;background:var(--blue);color:var(--white);text-align:center;line-height:30px;font-size:12px;border-radius:2px}

.panel-head{height:30px;line-height:30px;text-align:center;color:var(--white);font-size:13px}
.clients{top:3087px;left:202px;width:434px}
.clients .panel-head{background:var(--band)}
.logos{display:grid;grid-template-columns:repeat(5,1fr);row-gap:30px;margin-top:38px}
.logo{font-weight:700;font-size:12px;color:#3a3f44;text-align:center}
.social{top:3087px;left:646px;width:352px}
.social .panel-head{background:var(--red)}
.widget{margin-top:12px;padding:0 10px;font-size:11px;color:#444}
.widget .row{display:flex;align-items:center;gap:8px}
.widget .pic{width:40px;height:40px;background:var(--red)}
.widget .likebtn{width:40px;height:14px;background:#5a6f9b;margin-top:4px}
.faces{margin-top:6px;width:318px;height:92px;background:linear-gradient(135deg,#c8cbce,#9ea3a8)}

.footer{top:3395px;left:0;width:1200px;height:301px;background:var(--footer);color:#8d9398;font-size:12px}
.footer h5{font-family:"Montserrat",sans-serif;font-size:13px;color:#dfe2e4;font-weight:700;text-transform:uppercase;margin-bottom:28px}
.footer .col{position:absolute;top:64px}
.footer .col p{line-height:20px;margin-bottom:6px}
.footer .addr{display:flex;gap:8px;align-items:center;margin-bottom:16px}
.footer .socials{display:flex;gap:8px;margin-top:10px}
.footer .socials span{width:24px;height:24px;border-radius:50%;background:#5e656b}
.footer .copy{position:absolute;bottom:18px;width:100%;text-align:center;font-size:10px;color:#5f666c}
</style>
</head>
<body>

<header class="abs topbar">
  <div class="abs brand">KELVAPORT</div>
  <div class="abs item" style="left:468px">
    <svg width="16" height="14" viewBox="0 0 16 14"><path d="M2 1h12a1 1 0 0 1 1 1v7a1 1 0 0 1-1 1H7l-4 3v-3H2a1 1 0 0 1-1-1V2a1 1 0 0 1 1-1z" fill="#fff"/></svg>Chat Now
  </div>
  <div class="abs item" style="left:598px">
    <svg width="14" height="14" viewBox="0 0 14 14"><path d="M3 1l2 3-1.5 1.5a8 8 0 0 0 5 5L10 9l3 2-1.5 2.5C6 13 1 8 .5 2.5z" fill="#fff"/></svg>+41 (0) 31 482 17 90
  </div>
  <div class="abs item" style="left:983px">Login</div>
  <div class="abs item" style="left:1035px">Sign Up</div>
  <div class="abs item" style="left:1107px"><svg width="12" height="12" viewBox="0 0 12 12"><rect width="12" height="12" fill="#fff"/><path d="M5 2h2v3h3v2H7v3H5V7H2V5h3z" fill="#d8251c"/></svg></div>
</header>

<nav class="abs mainnav">
  <a class="active">Home</a><a>Unmanaged Swiss VPS</a><a>Swiss Web Hosting</a><a>Secure Swiss Email</a><a>Blog – Swiss Hosting</a><a>Contact Us</a>
</nav>

<section class="abs hero" role="img" aria-label="Faint light grey world map texture behind the hero headline">
  <h1>SOLID SWISS HOSTING</h1>
  <p>Get high quality unmanaged virtual private servers starting from <b>8 €</b> with <b>512MB ECC RAM</b> and <b>10 GB</b> of <b>SSD RAID</b> 10 hard disk space or super fast <b>SSD</b> hosting.</p>
  <div class="abs dots"><span></span><span></span><span class="on"></span><span></span></div>
</section>

<div class="abs strip"></div>
<div class="abs tiles">
  <div class="tile"><svg width="16" height="16" viewBox="0 0 16 16"><rect width="16" height="16" rx="2" fill="#2a2f34"/><path d="M4 8l3 3 5-6" stroke="#fff" stroke-width="2" fill="none"/></svg>Ideal for Small<br>file or data bases</div>
  <div class="tile"><svg width="16" height="16" viewBox="0 0 16 16"><rect width="16" height="16" rx="2" fill="#2a2f34"/><path d="M4 8l3 3 5-6" stroke="#fff" stroke-width="2" fill="none"/></svg>500 MB per second<br>read &amp; write</div>
  <div class="tile"><svg width="16" height="16" viewBox="0 0 16 16"><rect width="16" height="16" rx="2" fill="#2a2f34"/><path d="M4 8l3 3 5-6" stroke="#fff" stroke-width="2" fill="none"/></svg>Less Power<br>Consumption</div>
  <div class="tile"><svg width="16" height="16" viewBox="0 0 16 16"><rect width="16" height="16" rx="2" fill="#2a2f34"/><path d="M4 8l3 3 5-6" stroke="#fff" stroke-width="2" fill="none"/></svg>Strong backup<br>support</div>
  <div class="tile"><svg width="16" height="16" viewBox="0 0 16 16"><rect width="16" height="16" rx="2" fill="#2a2f34"/><path d="M4 8l3 3 5-6" stroke="#fff" stroke-width="2" fill="none"/></svg>Quickly<br>backup offsite</div>
  <div class="tile"><svg width="16" height="16" viewBox="0 0 16 16"><rect width="16" height="16" rx="2" fill="#2a2f34"/><path d="M4 8l3 3 5-6" stroke="#fff" stroke-width="2" fill="none"/></svg>Dailydata store<br>onsite</div>
</div>

<div class="abs sec-title-1"><h2 class="heading" style="font-size:25px">Swiss Hosting - VPS in Switzerland</h2><div class="rule"></div></div>
<div class="abs tabs"><span>Swiss Web Hosting</span><span class="on">Unmanaged Swiss VPS</span><span>Secure Swiss Email</span><span>Reviews</span><span>FAQ's</span></div>

<div class="abs card" style="left:135px">
  <div class="head">SSD Unmanaged<br>VPS 512MB<div class="price"><span class="cur">€</span><span class="num">8</span><span class="per">per month</span></div></div>
  <ul><li>2 CPU cores (QVR 1)</li><li>20 GB datacenter SSD disk</li><li>space</li><li>100GB bandwidth</li><li>512MB ECC RAM</li><li>1 dedicated IP addresses</li><li>100 Mbit connection</li></ul>
  <div class="buy">Purchase Corevirt</div>
</div>
<div class="abs card" style="left:374px">
  <div class="head">SSD Unmanaged<br>VPS 1024MB<div class="price"><span class="cur">€</span><span class="num">14</span><span class="per">per month</span></div></div>
  <ul><li>4 CPU cores (QVR 2)</li><li>30 GB datacenter SSD disk</li><li>space</li><li>200GB bandwidth</li><li>1024MB ECC RAM</li><li>1 dedicated IP addresses</li><li>100 Mbit connection</li></ul>
  <div class="buy">Purchase Corevirt</div>
</div>
<div class="abs card" style="left:613px">
  <div class="head">SSD Unmanaged<br>VPS 2048MB<div class="price"><span class="cur">€</span><span class="num">24</span><span class="per">per month</span></div></div>
  <ul><li>4 CPU cores (QVR 2)</li><li>40 GB datacenter SSD disk</li><li>space</li><li>500GB bandwidth</li><li>2048MB ECC RAM</li><li>1 dedicated IP addresses</li><li>100 Mbit connection</li></ul>
  <div class="buy">Purchase Corevirt</div>
</div>
<div class="abs card" style="left:852px">
  <div class="head">SSD Unmanaged<br>VPS 512MB<div class="price"><span class="cur">€</span><span class="num">41</span><span class="per">per month</span></div></div>
  <ul><li>4 CPU cores (QVR 4)</li><li>60 GB datacenter SSD disk</li><li>space</li><li>2TB bandwidth</li><li>4096MB ECC RAM</li><li>1 dedicated IP addresses</li><li>100 Mbit connection</li></ul>
  <div class="buy">Purchase Corevirt</div>
</div>

<div class="abs btn-green" style="top:1096px;left:513px;width:174px;height:37px;line-height:37px">Get Started</div>

<section class="abs helpbar">
  <div class="abs item" style="left:79px">Need Any Help ?</div>
  <div class="abs item" style="left:490px">
    <svg width="22" height="20" viewBox="0 0 22 20"><path d="M3 12V10a8 8 0 0 1 16 0v2" stroke="#fff" stroke-width="2.4" fill="none"/><rect x="1" y="11" width="5" height="8" rx="1.5" fill="#fff"/><rect x="16" y="11" width="5" height="8" rx="1.5" fill="#fff"/></svg>+41 (0) 31 482 17 90
  </div>
  <div class="abs item" style="left:868px">
    <svg width="18" height="18" viewBox="0 0 18 18"><path d="M1 8L17 1 12 17 9 10z" fill="#fff"/></svg>webmaster@kelvaport.ch
  </div>
</section>

<div class="abs sec-title-2"><h2 class="heading" style="font-size:25px">Swiss Hosting - VPS in Switzerland</h2><div class="rule"></div></div>
<div class="abs ben-head-red">SSD only offerings and therefore amazing benefits</div>
<div class="abs ben-head-dark">Regular backups for Corevirt VPS to<br>keep your data safe</div>

<div class="abs" style="top:1510px;left:81px;width:1035px;height:185px">
  <div class="abs ben" style="left:0;top:0"><span class="n">1</span><div class="icon"><svg width="22" height="22" viewBox="0 0 22 22"><ellipse cx="11" cy="5" rx="8" ry="3" fill="#fff"/><path d="M3 8c0 4 16 4 16 0v4c0 4-16 4-16 0zM3 14c0 4 16 4 16 0v3c0 4-16 4-16 0z" fill="#fff"/></svg></div>Incredible performance because of virtually instantaneous data access times, low <span class="more">(...)</span></div>
  <div class="abs ben" style="left:172px;top:0"><span class="n">2</span><div class="icon"><svg width="22" height="22" viewBox="0 0 22 22"><circle cx="11" cy="12" r="8" stroke="#fff" stroke-width="2" fill="none"/><path d="M11 12l4-4M9 2h4" stroke="#fff" stroke-width="2"/></svg></div>Expedient data read and write rates of above 500 MB per second</div>
  <div class="abs ben" style="left:344px;top:0"><span class="n">3</span><div class="icon"><svg width="24" height="18" viewBox="0 0 24 18"><path d="M1 8l5-5 6 3 6-3 5 5-7 7-4-3-4 3z" fill="#fff"/></svg></div>Due to the lack of moving parts there is extreme reliability</div>
  <div class="abs ben" style="left:516px;top:0"><span class="n">4</span><div class="icon"><svg width="18" height="22" viewBox="0 0 18 22"><path d="M9 1a7 7 0 0 0-4 13v3h8v-3A7 7 0 0 0 9 1z" fill="#fff"/><rect x="6" y="18" width="6" height="3" fill="#fff"/></svg></div>Less power consumption and lower cooling requirements</div>
  <div class="abs ben" style="left:688px;top:0"><span class="n">5</span></div>
  <div class="abs ben" style="left:863px;top:0"><span class="n">6</span><div class="icon"><svg width="20" height="20" viewBox="0 0 20 20"><path d="M2 2h13l3 3v13H2z" fill="#fff"/><rect x="5" y="2" width="8" height="5" fill="#2d3338"/><rect x="5" y="11" width="10" height="5" fill="#2d3338"/></svg></div>SSD virtual private servers have 1x daily and 1x weekly backup where it can be <span class="more">(...)</span></div>
</div>
<div class="abs ben-pop">Kelvaport Webhosting includes daily backups with a incredible retention policy (...) (7x daily, 5x weekly and 12 monthly backups are kept on- and offsite). Additionally users can choose on their own for additional backup strategies directly from their hosting panel
  <svg class="abs" style="right:8px;bottom:8px" width="8" height="10" viewBox="0 0 8 10"><path d="M0 0l8 5-8 5z" fill="#fff"/></svg></div>

<div class="abs btn-green" style="top:1794px;left:546px;width:108px;height:29px;line-height:29px;font-size:12px">Learn more</div>
<div class="abs about-link">about Swiss VPS hosting or the benefits of offshore hosting</div>

<section class="abs offshore" role="img" aria-label="Dark section with faint world map pattern in the background">
  <h2 class="heading">Benefits of offshore hosting in Switzerland<div class="rule"></div></h2>
  <div class="abs flags">
    <svg width="26" height="26" viewBox="0 0 26 26"><rect width="26" height="26" fill="#d8251c" transform="rotate(-10 13 13)"/><path d="M11 6h4v5h5v4h-5v5h-4v-5H6v-4h5z" fill="#fff"/></svg>
    <svg width="26" height="26" viewBox="0 0 26 26"><rect width="26" height="26" fill="#d8251c" transform="rotate(10 13 13)"/><path d="M11 6h4v5h5v4h-5v5h-4v-5H6v-4h5z" fill="#fff"/></svg>
  </div>
  <p class="sub">Incredible data protection and privacy thanks to hosting offshore</p>
  <ul>
    <li>Benefit from a solid hosting experience within Switzerland where your data is protected by Swiss privacy laws and Swiss federal data protection regulations (DPA)</li>
    <li>High quality standards for used hardware and our datacenter</li>
    <li>No electronic data exchange with other governments in case of the absence of criminal activity</li>
  </ul>
</section>

<section class="abs aswell">
  <h3>As well as</h3>
  <p>High quality servers by Dravonex which deliver superior server choice that can reliably support any workload<br>
  Guaranteed server resources for all hosting packages and virtual private servers. We do not oversell our servers<br>
  Profit from one of the best offshore hosting experiences available<br>
  Affordable offshore hosting and top offshore hoster = Kelvaport.ch</p>
</section>
<div class="abs notch" style="top:2328px;border-top:12px solid #31383e"></div>

<div class="abs sec-title-3"><h2 class="heading" style="font-size:25px">Visit the Kelvaport.ch blog</h2></div>
<div class="abs arrow" style="left:130px">‹</div>
<div class="abs arrow" style="left:1050px">›</div>
<article class="abs post" style="left:197px">
  <div class="avatar" role="img" aria-label="Author portrait"></div>
  <h4>Benefits of a Swiss VPS</h4>
  <div class="meta">by <b>Lukas Imhof</b> Apr 14, 2016, 3h <svg width="12" height="10" viewBox="0 0 12 10"><path d="M0 0h12v7H5l-3 3V7H0z" fill="#d8251c"/></svg>10</div>
  <p class="body">High quality servers by Dravonex which deliver superior server choice that can reliably Guaranteed server resources for all hosting packages and virtual private servers.</p>
  <div class="read">Read More</div>
</article>
<article class="abs post" style="left:653px">
  <div class="avatar" role="img" aria-label="Author portrait"></div>
  <h4>Benefits of a Swiss VPS</h4>
  <div class="meta">by <b>Lukas Imhof</b> Apr 14, 2016, 3h <svg width="12" height="10" viewBox="0 0 12 10"><path d="M0 0h12v7H5l-3 3V7H0z" fill="#d8251c"/></svg>10</div>
  <p class="body">High quality servers by Dravonex which deliver superior server choice that can reliably Guaranteed server resources for all hosting packages and virtual private servers.</p>
  <div class="read">Read More</div>
</article>

<section class="abs promo"><div class="mid"></div></section>
<div class="abs badge"><div class="inner">40<span>%<small>Offer</small></span></div></div>
<div class="abs promo-text">Save 40%, Offer Ends on</div>
<div class="abs promo-btn">Learn more</div>

<section class="abs clients">
  <div class="panel-head">Our happy clients</div>
  <div class="logos">
    <div class="logo">Tarvelon</div><div class="logo">Quimbrex</div><div class="logo">Aerovask</div><div class="logo">Brundelo</div><div class="logo">Mortaxi</div>
    <div class="logo">Skelvaro</div><div class="logo">Rolvendt</div><div class="logo">Optrisk</div><div class="logo">Hopvaldt</div><div class="logo">Strundex</div>
    <div class="logo">Nexquor</div><div class="logo">Alpivar</div><div class="logo">Vintrelo</div><div class="logo">Fizzomar</div><div class="logo">Lumvaxo</div>
  </div>
</section>
<section class="abs social">
  <div class="panel-head">1,39,859 customers liked us on Circlebook</div>
  <div class="widget">
    <div class="row"><div class="pic"></div><div><b>KELVAPORT</b><div class="likebtn"></div></div></div>
    <p style="margin-top:8px">108 people like Kelvaport.</p>
    <div class="faces" role="img" aria-label="Grid of follower profile pictures"></div>
    <p style="margin-top:6px;font-size:9px;color:#777">Circlebook social plugin</p>
  </div>
</section>

<footer class="abs footer">
  <div class="col" style="left:79px;width:180px"><h5>About Us</h5><p>We are a young start up that combines solid open source software with innovative hosting solutions</p></div>
  <div class="col" style="left:333px"><h5>Services</h5><p>Unmanaged Swiss VPS</p><p>Swiss Web Hosting</p><p>Secure Swiss Email</p><p>Benefits of offshore hosting</p><p>Swiss data protection</p></div>
  <div class="col" style="left:623px"><h5>Company Information</h5><p>Announcements</p><p>Knowledgebase</p><p>Network Status</p></div>
  <div class="col" style="left:941px"><h5>Our Address</h5>
    <div class="addr"><svg width="10" height="14" viewBox="0 0 10 14"><path d="M5 0a5 5 0 0 1 5 5c0 4-5 9-5 9S0 9 0 5a5 5 0 0 1 5-5z" fill="#8d9398"/></svg>Talweg 12, 8050 Zurich, CH</div>
    <div class="addr"><svg width="12" height="12" viewBox="0 0 14 14"><path d="M3 1l2 3-1.5 1.5a8 8 0 0 0 5 5L10 9l3 2-1.5 2.5C6 13 1 8 .5 2.5z" fill="#8d9398"/></svg>+41 (0) 31 482 17 90</div>
    <div class="addr"><svg width="12" height="10" viewBox="0 0 12 10"><rect width="12" height="10" fill="#8d9398"/><path d="M0 0l6 5 6-5" stroke="#24282c" fill="none"/></svg>webmaster@kelvaport.ch</div>
    <div class="socials"><span></span><span></span><span></span></div>
  </div>
  <div class="copy">Copyright 2016 Kelvaport. All rights reserved.</div>
</footer>

</body>
</html>
```